Animal care facility (Pet Grooming, Doggie daycare, Boarding, Pet Boutique)

Hi there! i came across your wonderful work and would love to work with you! I have a clear image in my head that i want for my bussiness card and stationary. I will go ahead and attach pictures of business cards that i have found to give you an idea of what i would like to see.

My color scheme is a gray back ground and white lettering. So for the card i would like it to be a gray and the logo on the front to be white and done like picture #1. I would like the quality of the card to be a thicker more durable look. I would want just my logo and then underneath my name ( Marisa Thornbury and my title Owner similar to picture #1. I also have somone i am working with so his would need to be (Colin Pratt, General Manager)

Also there is certain information that does need to be on the back of the card so I don't know if a white back with gray lettering would help it be easily read or not.

Alderwick Pet Haven & Spa LLC
862 E. Millrace Rd.
507.264.1193 -Phone
507.268.4410-Fax
Info@alderwickpethavenandspa.com-Email

Grooming- Boarding-Daycare-Pet Boutique

$10.00 OFF First Time Grooming Visit

The font for all of this is using (oranienbaum)
next to the phone fax, email I would like the actual small pictures that I have in one of the photos
Updates

Industry/Entity Type

Pet Care

Requirements
Must have
• Please follow the design of picture 7 I would like to change the direction of the card all together now. I would like the image to be up top and the name and title to be laid out the same and also in the same font as the attached picture. Again I would like all of this on the front to be engraved In white foil on gray matte backing and if we could lighten the color of this card up I would appreciate it but be on the darker side.
• On the back side keep the version you made and flip all the information to be laid out vertically just like the front.

```html
<!DOCTYPE html>
<html lang="en">
<head>
<meta charset="utf-8">
<title>Alderwick Pet Haven &amp; Spa — Stationery</title>
<link rel="stylesheet" href="https://fonts.googleapis.com/css2?family=Oranienbaum&family=Arimo:wght@400;700&family=Cookie&display=swap">
<style>
:root{
  --stage:#000;
  --paper:#fbfbfb;
  --slate:#2d3032;
  --band:#33363c;
  --ink:#1f2124;
  --foil:#f4f4f4;
  --serif:'Oranienbaum', Georgia, serif;
  --sans:'Arimo', Arial, sans-serif;
  --script:'Cookie', cursive;
}
*{box-sizing:border-box;margin:0;padding:0}
html,body{width:1189px;height:1200px;overflow:hidden;background:var(--stage)}
.canvas{position:relative;width:1189px;height:1200px}
.sheet,.card{position:absolute;overflow:hidden}
.frame{position:absolute;inset:0;width:100%;height:100%}
.frame path{fill:none;stroke:var(--foil);stroke-width:1.3}

/* brand block */
.brand{position:absolute;display:flex;flex-direction:column;align-items:center;text-align:center}
.brand-mark{border-radius:50%;border:1.5px solid currentColor}
.brand-name{font-family:var(--serif);text-transform:uppercase;line-height:1.15;letter-spacing:.02em}

/* letterhead */
.letterhead{left:75px;top:55px;width:507px;height:656px;background:var(--paper);color:var(--ink)}
.letterhead .brand{left:30px;top:30px;width:135px;color:var(--ink)}
.letterhead .brand-mark{width:54px;height:54px;margin-bottom:8px}
.letterhead .brand-name{font-size:14px}
.lh-contact{position:absolute;left:308px;top:76px;border-left:1px solid var(--ink);padding-left:6px;font-family:var(--serif);font-size:8px;line-height:10.5px}
.lh-contact li{list-style:none;display:flex;align-items:center;gap:4px}
.lh-contact svg{width:7px;height:7px;fill:var(--ink)}
.recipient{position:absolute;left:40px;top:183px;font-family:var(--sans);font-size:7.6px;line-height:10px}
.recipient strong{display:block;font-size:9px;margin-bottom:5px;font-weight:400;letter-spacing:.02em}
.letter-body{position:absolute;left:40px;top:249px;width:428px;font-family:var(--sans);font-size:8.4px;line-height:14.8px;text-align:justify}
.letter-body p+p{margin-top:14px}
.closing{font-family:var(--sans);font-size:8.4px;line-height:11px}
.signature{position:absolute;left:40px;top:478px;font-family:var(--script);font-size:34px;line-height:1}
.signer{position:absolute;left:40px;top:522px;font-family:var(--sans);font-size:8.6px;line-height:11px}
.lh-footer{position:absolute;left:0;right:0;bottom:0;height:33px;background:var(--band);color:var(--foil);font-family:var(--serif);font-size:12.5px;display:flex;align-items:center;justify-content:center;letter-spacing:.02em}

/* dark sheet */
.slate-sheet{left:613px;top:56px;width:505px;height:652px;background:var(--slate);color:var(--foil)}
.slate-sheet .brand{left:0;right:0;top:92px}
.slate-sheet .brand-mark{width:64px;height:64px;margin-bottom:10px}
.slate-sheet .brand-name{font-size:16px}
.sheet-services{position:absolute;left:0;right:0;top:586px;text-align:center;font-family:var(--serif);font-size:12.5px;letter-spacing:.02em}

/* cards */
.card{background:var(--slate);color:var(--foil)}
.card-front{left:342px;top:778px;width:199px;height:349px}
.card-back{left:646px;top:772px;width:203px;height:357px}
.card-front .brand{left:0;right:0;top:66px}
.card-front .brand-mark{width:58px;height:58px;margin-bottom:10px}
.card-front .brand-name{font-size:14.5px}
.holder{position:absolute;left:0;right:0;top:262px;text-align:center;font-family:var(--script);line-height:1}
.holder-name{font-size:21px}
.holder-title{font-size:14px;margin-top:-2px}
.card-back .brand{left:0;right:0;top:48px}
.card-back .brand-mark{width:48px;height:48px;margin-bottom:8px}
.card-back .brand-name{font-size:12.5px}
.back-services{position:absolute;left:0;right:0;top:178px;text-align:center;font-family:var(--serif);font-size:11px;line-height:14px}
.offer{position:absolute;left:0;right:0;top:232px;text-align:center;font-family:var(--serif);font-size:9px}
.back-contact{position:absolute;right:19px;top:259px;font-family:var(--serif);font-size:9px;line-height:13px;text-align:right}
.back-contact li{list-style:none;display:flex;justify-content:flex-end;align-items:center;gap:4px}
.back-contact svg{width:7px;height:7px;fill:var(--foil)}
</style>
</head>
<body>
<svg width="0" height="0" style="position:absolute" aria-hidden="true">
  <defs>
    <symbol id="ico-pin" viewBox="0 0 10 10"><path d="M5 0a3.6 3.6 0 0 0-3.6 3.6C1.4 6.3 5 10 5 10s3.6-3.7 3.6-6.4A3.6 3.6 0 0 0 5 0zm0 5a1.4 1.4 0 1 1 0-2.8A1.4 1.4 0 0 1 5 5z"/></symbol>
    <symbol id="ico-phone" viewBox="0 0 10 10"><path d="M2.2 0 3.8 2.2 2.9 3.3a6 6 0 0 0 3.8 3.8l1.1-.9L10 7.8 8.6 9.6C4.5 10 0 5.5.4 1.4z"/></symbol>
    <symbol id="ico-fax" viewBox="0 0 10 10"><path d="M2.5 0h5v3h-5zM0 3.5h10V8H8v2H2V8H0zm3 3V9h4V6.5z"/></symbol>
    <symbol id="ico-mail" viewBox="0 0 10 10"><path d="M0 2h10v.8L5 5.8 0 2.8zm0 1.9 5 3 5-3V8H0z"/></symbol>
  </defs>
</svg>

<main class="canvas">

  <section class="sheet letterhead" aria-label="Letterhead">
    <div class="brand">
      <span class="brand-mark"></span>
      <span class="brand-name">Alderwick Pet<br>Haven &amp; Spa</span>
    </div>
    <ul class="lh-contact">
      <li><svg><use href="#ico-pin"/></svg>862 E. Millrace Rd.</li>
      <li><svg><use href="#ico-phone"/></svg>507.264.1193</li>
      <li><svg><use href="#ico-fax"/></svg>507.268.4410</li>
      <li><svg><use href="#ico-mail"/></svg>Info@alderwickpethavenandspa.com</li>
    </ul>
    <div class="recipient">
      <strong>EVAN MARSH</strong>
      Street Name,City Name.<br>Zip Coad 0000
    </div>
    <div class="letter-body">
      <p>Lorem Ipsum is simply dummy text of the printing and typesetting industry. Lorem Ipsum has been the industry's standard dummy text ever since the 1500s, when an unknown printer took a galley of type and scrambled it to make a type specimen book. It has survived not only five centuries,but also the leap into electronic typesetting, remaining essentially unchanged. It was popularised in the 1960s with the release of Tranfex sheets containing Lorem Ipsum passages, and more recently with desktop publishing software like Pressline Composer including versions of Lorem Ipsum.</p>
      <p>It is a long established fact that a reader will be distracted by the readable content of a page when looking at its layout. The point of using Lorem Ipsum is that it has a more-or-less normal distribution of letters, as opposed to using 'Content here, content here', making it look like readable English. Many desktop and publishing packages and web page editors now use Lorem Ipsum as their default model text, and a search for 'lorem ipsum' will uncover many web sites still in their infancy. Various versions have evolved over the years, sometimes by accident, sometimes on purpose (injected humour and the like).</p>
      <p class="closing" style="margin-top:0">Regards,</p>
    </div>
    <div class="signature">Paul Reed</div>
    <div class="signer">Paul Reed<br>General Maneger</div>
    <footer class="lh-footer">Grooming | Boarding | Daycare | Pet Boutique</footer>
  </section>

  <section class="sheet slate-sheet" aria-label="Folder cover">
    <svg class="frame" viewBox="0 0 505 652" aria-hidden="true">
      <path d="M47 20H458A18 18 0 0 0 476 38V614A18 18 0 0 0 458 632H47A18 18 0 0 0 29 614V38A18 18 0 0 0 47 20Z"/>
      <path d="M50 25H455A16 16 0 0 0 471 41V611A16 16 0 0 0 455 627H50A16 16 0 0 0 34 611V41A16 16 0 0 0 50 25Z"/>
    </svg>
    <div class="brand">
      <span class="brand-mark"></span>
      <span class="brand-name">Alderwick Pet<br>Haven &amp; Spa</span>
    </div>
    <p class="sheet-services">Grooming | Boarding | Daycare | Pet Boutique</p>
  </section>

  <section class="card card-front" aria-label="Business card front">
    <svg class="frame" viewBox="0 0 199 349" aria-hidden="true">
      <path d="M21 8H178A11 11 0 0 0 189 19V330A11 11 0 0 0 178 341H21A11 11 0 0 0 10 330V19A11 11 0 0 0 21 8Z"/>
      <path d="M23 12H176A9 9 0 0 0 185 21V328A9 9 0 0 0 176 337H23A9 9 0 0 0 14 328V21A9 9 0 0 0 23 12Z"/>
    </svg>
    <div class="brand">
      <span class="brand-mark"></span>
      <span class="brand-name">Alderwick Pet<br>Haven &amp; Spa</span>
    </div>
    <div class="holder">
      <div class="holder-name">Marisa Thornbury</div>
      <div class="holder-title">Owner</div>
    </div>
  </section>

  <section class="card card-back" aria-label="Business card back">
    <svg class="frame" viewBox="0 0 203 357" aria-hidden="true">
      <path d="M21 8H182A11 11 0 0 0 193 19V338A11 11 0 0 0 182 349H21A11 11 0 0 0 10 338V19A11 11 0 0 0 21 8Z"/>
      <path d="M23 12H180A9 9 0 0 0 189 21V336A9 9 0 0 0 180 345H23A9 9 0 0 0 14 336V21A9 9 0 0 0 23 12Z"/>
    </svg>
    <div class="brand">
      <span class="brand-mark"></span>
      <span class="brand-name">Alderwick Pet<br>Haven &amp; Spa</span>
    </div>
    <p class="back-services">Grooming | Boarding | Daycare<br>Pet Boutique</p>
    <p class="offer">$10.00 OFF First Time Grooming Visit</p>
    <ul class="back-contact">
      <li>862 E. Millrace Rd.<svg><use href="#ico-pin"/></svg></li>
      <li>507.264.1193<svg><use href="#ico-phone"/></svg></li>
      <li>507.268.4410<svg><use href="#ico-fax"/></svg></li>
      <li>Info@alderwickpethavenandspa.com<svg><use href="#ico-mail"/></svg></li>
    </ul>
  </section>

</main>
</body>
</html>
```